American Painting Company Needs YOU to Design Their Website [Descriptive Brief]

A house painting company based in Knoxville TN, USA needs a fresh, new, fun, and playful--yet, simple, elegant and professional--website made. Here is a link to their existing site:

http://www.brightoakcoatings.example/

We want to keep the same site structure, so the navigation layout will stay the same. However, the video is too small, is too far over in the sidebar, and the overall design is amateur at best. We want something bright, colorful and bold! However, keep in mind the logo in the upper left of the header: The color scheme must include that red, white, and gray.

Here are some examples to look at to get your creative juices flowing!

http://lumenbrushworks.example/

http://www.wfcg.example/

http://www.halvorsen-pike.example/

http://www.tidyframepages.example/painting-company-niche-website/

http://www.quillgridstudio.example/website-templates/painting-company-website-template-83172.html

We have accounts at both pixmeadow.example and snapvault.example. If you use placeholder images from there, that's fine. We can buy the images when and if your design is selected.

Target Market(s)

The audience is the average middle class homeowner. This should appeal to families, couples, and singles who own a home.

Industry/Entity Type

House

Requirements
Must have
• - Lots of color! It's a site about painting homes. People like a variety of colors. Bring out your inner artist, and get bold with your colors!
• - A video place holder. As you can see, there is a video on the existing site, but it's small and hidden. Make it big and put it top left, or in the center.
• -Detailed and organized PSD structure. We're going to turn your design into a website, and to make that work soothly, we ask that you organize you PSD well: name your layers, keep things separated, group and ungroup as necessary, etc.
• A sidebar that goes down the right side of an interior page. We need a homepage, and also one [1] interior page template. We don't need you to make a design for each page. Just the homepage, followed by a simple interior page design that requires only the header/navigation, and a sidebar down the right side.
Should not have
• Coding. This is a design project only.

```html
<!DOCTYPE html>
<html lang="en">
<head>
<meta charset="utf-8">
<title>Brightoak Coatings – Residential &amp; Commercial Painting</title>
<link rel="stylesheet" href="https://fonts.googleapis.com/css2?family=Arimo:wght@400;700&family=PT+Sans:wght@400;700&display=swap">
<style>
  :root {
    --red: #b5121b;
    --red-deep: #8e0d16;
    --red-dark: #6a0a10;
    --pink-band: #e9b9bd;
    --pink-soft: #f6e0e2;
    --footer: #b86f73;
    --footer-dark: #a35a5f;
    --bottom: #6d0a12;
    --grey-text: #555;
    --heading: #5a4a4a;
    --line: #cfcfcf;
    --white: #fff;
    --lime: #c8dc7a;
  }
  * { box-sizing: border-box; margin: 0; padding: 0; }
  html, body { width: 1200px; height: 1042px; overflow: hidden; }
  body {
    position: relative;
    font-family: "Arimo", Arial, sans-serif;
    color: var(--grey-text);
    background: linear-gradient(180deg, var(--pink-band) 0, var(--pink-band) 340px, var(--pink-soft) 560px, #fff 760px, #fff 100%);
  }
  .abs { position: absolute; }

  /* Header */
  .masthead {
    position: absolute; left: 0; top: 0; width: 1200px; height: 285px;
    background: radial-gradient(ellipse at 50% 40%, #a8141e 0, var(--red-deep) 70%, #7d0b13 100%);
  }
  .masthead-band { position: absolute; left: 0; top: 285px; width: 1200px; height: 43px; background: var(--red-dark); }
  .masthead-rule { position: absolute; left: 0; top: 328px; width: 1200px; height: 10px; background: #f7eeee; }

  .brand {
    left: 189px; top: 9px; width: 163px; height: 127px; background: #fff;
    display: flex; align-items: center; justify-content: center; gap: 6px; flex-direction: column;
  }
  .brand-mark { width: 34px; height: 34px; background: var(--red); }
  .brand-name { font-family: "PT Sans", sans-serif; font-weight: 700; font-size: 19px; color: var(--red); text-align: center; line-height: 1.05; }

  .utility { right: 206px; top: 13px; display: flex; align-items: center; font-size: 11px; color: #fff; }
  .utility a { color: #fff; text-decoration: none; }
  .utility .current { background: var(--red); padding: 3px 7px; border-radius: 2px; margin-right: 6px; }
  .utility .sep { margin: 0 6px; }

  .callout { left: 527px; top: 64px; color: #fff; font-family: "PT Sans", sans-serif; }
  .callout small { display: block; font-size: 13.5px; font-weight: 700; }
  .callout strong { display: block; font-size: 27px; font-weight: 400; letter-spacing: .3px; line-height: 1.1; }

  .finder { left: 750px; top: 63px; color: #fff; font-family: "PT Sans", sans-serif; }
  .finder label { display: block; font-size: 13.5px; font-weight: 700; margin-bottom: 5px; }
  .finder-row { display: flex; }
  .finder-input { width: 177px; height: 21px; background: #fff; border: 1px solid #ddd; font-size: 9.5px; color: #777; padding: 5px 7px; font-family: "Arimo", sans-serif; }
  .finder-button { width: 70px; height: 21px; margin-left: 2px; background: var(--red); color: #fff; font-size: 11px; font-weight: 700; display: flex; align-items: center; justify-content: center; gap: 3px; }

  /* Navigation */
  .nav { left: 179px; top: 146px; width: 821px; height: 34px; background: #f5f5f5; display: flex; align-items: stretch; font-family: "Arimo", Arial, sans-serif; font-size: 12px; font-weight: 700; color: #555; }
  .nav a { color: #555; text-decoration: none; display: flex; align-items: center; justify-content: center; flex: 1 1 auto; padding: 0 6px; white-space: nowrap; }
  .nav a.active { background: var(--red); color: #fff; flex: 0 0 73px; }

  /* Hero */
  .hero { left: 179px; top: 180px; width: 821px; height: 326px;
    background: linear-gradient(120deg, #5e88c9 0, #d8e4f2 22%, #b0a694 45%, #f3a23a 65%, #f07a45 82%, #f5b3a8 100%); }
  .hero-tag { left: 200px; top: 352px; width: 171px; height: 130px; background: rgba(20,20,20,.88);
    font-family: "PT Sans", sans-serif; color: #fff; padding: 34px 0 0 12px; line-height: .98; }
  .hero-tag span { display: block; font-size: 28px; letter-spacing: -.5px; }
  .hero-tag .accent { color: var(--lime); font-weight: 700; }

  /* Feature row */
  .welcome { left: 179px; top: 515px; width: 265px; height: 193px; background: linear-gradient(160deg, #3b3a1e, #17120e 50%, #3d3515); padding: 4px; }
  .welcome-inner { position: relative; height: 100%; background: rgba(15,12,10,.82); }
  .panel-title { background: var(--red); color: #fff; font-family: "PT Sans", sans-serif; font-weight: 700; font-size: 15px; padding: 5px 11px; }
  .welcome p { color: #fff; font-size: 9.4px; line-height: 15px; text-align: justify; padding: 6px 9px 0 9px; }
  .welcome .more { position: absolute; left: 9px; right: 9px; bottom: 7px; border-top: 1px solid #555; padding-top: 5px; text-align: right; color: #fff; font-size: 9.5px; }

  .video { left: 456px; top: 515px; width: 266px; height: 193px; background: linear-gradient(180deg, #7b1030 0, #7b1030 33%, #ededed 33%, #dcdcdc 100%); }
  .video-play { left: 583px; top: 597px; width: 36px; height: 26px; background: #1c1c1c; border-radius: 4px; display: flex; align-items: center; justify-content: center; }
  .video-caption { left: 461px; top: 676px; width: 257px; height: 28px; background: var(--red); color: #fff; font-family: "PT Sans", sans-serif; font-weight: 700; font-size: 14.5px; padding: 5px 15px; }

  .estimate { left: 735px; top: 515px; width: 264px; height: 196px; background: #fff; border: 1px solid #e3c8ca; }
  .estimate .panel-title { font-size: 14.5px; padding: 6px 8px; }
  .field-label { font-size: 11px; font-weight: 700; color: #444; }
  .field { height: 19px; border: 1px solid #ccc; font-size: 9.5px; color: #888; padding: 3px 5px; }
  .radio { display: inline-flex; align-items: center; gap: 4px; font-size: 11px; font-weight: 700; color: #555; margin-right: 7px; }
  .radio i { width: 10px; height: 10px; border: 1px solid #999; border-radius: 50%; display: inline-block; position: relative; }
  .radio i.on::after { content: ""; position: absolute; left: 2px; top: 2px; width: 4px; height: 4px; border-radius: 50%; background: #4a9a4a; }
  .estimate-btn { background: var(--red); color: #fff; font-size: 12px; font-weight: 700; width: 70px; height: 21px; border-radius: 3px; display: flex; align-items: center; justify-content: center; }

  /* Stories */
  .story { top: 752px; width: 255px; }
  .story-head { display: flex; justify-content: space-between; align-items: center; border-bottom: 1px solid var(--line); padding-bottom: 6px; font-family: "PT Sans", sans-serif; font-size: 14.5px; font-weight: 700; color: var(--heading); }
  .story-arrow { width: 16px; height: 16px; border-radius: 50%; background: #c8c8c8; display: flex; align-items: center; justify-content: center; }
  .story-body { display: flex; gap: 8px; margin-top: 9px; }
  .story-thumb { width: 60px; height: 56px; flex: none; }
  .story-body h4 { font-size: 10.5px; color: #4a2020; margin-bottom: 2px; }
  .story-body p { font-size: 9.7px; line-height: 14px; color: #666; text-align: justify; }
  .story-body a { display: inline-block; margin-top: 2px; font-size: 9px; color: #6a2020; }

  /* Footer */
  .footer { left: 0; top: 887px; width: 1200px; height: 116px; background: var(--footer); }
  .foot-col { top: 898px; color: #fff; }
  .foot-col h5 { font-family: "PT Sans", sans-serif; font-size: 13px; font-weight: 700; margin-bottom: 8px; width: 140px; border-bottom: 1px solid rgba(255,255,255,.25); padding-bottom: 6px; }
  .foot-col ul { list-style: none; font-size: 9.7px; line-height: 15.5px; }
  .foot-col li::before { content: "▸"; font-size: 7px; margin-right: 7px; }
  .foot-col .here { font-weight: 700; text-decoration: underline; }

  .foot-side { left: 640px; top: 887px; width: 359px; height: 116px; border-left: 1px solid rgba(255,255,255,.35); border-right: 1px solid rgba(255,255,255,.35); }
  .quote { left: 647px; top: 895px; width: 269px; height: 55px; background: var(--footer-dark); color: #fff; font-size: 9.5px; line-height: 14px; padding: 5px 9px; }
  .quote em { font-style: normal; color: #f1dcdc; }
  .quote u { color: #fff; }
  .quote-badge { left: 930px; top: 896px; width: 60px; text-align: center; color: #fff; font-size: 10px; font-weight: 700; }
  .quote-badge div { width: 34px; height: 34px; background: #f4f1ea; margin: 0 auto 4px; }
  .follow { left: 648px; top: 971px; display: flex; align-items: center; gap: 5px; color: #fff; font-size: 11px; font-weight: 700; }
  .follow b { margin-right: 6px; }
  .follow i { width: 20px; height: 20px; border-radius: 3px; display: inline-block; }
  .foot-divide { left: 640px; top: 957px; width: 359px; border-top: 1px solid rgba(255,255,255,.35); }
  .foot-call { left: 814px; top: 957px; width: 185px; height: 46px; border-left: 1px solid rgba(255,255,255,.35); color: #fff; font-family: "PT Sans", sans-serif; font-size: 16px; font-weight: 700; display: flex; align-items: center; justify-content: center; }

  .base { left: 0; top: 1003px; width: 1200px; height: 39px; background: var(--bottom); color: #fff; font-size: 10px; }
  .base .copy { position: absolute; left: 179px; top: 13px; }
  .base .copy b { text-decoration: underline; }
  .base .top { position: absolute; right: 201px; top: 11px; display: flex; align-items: center; gap: 8px; font-weight: 700; }
  .base .top span { width: 16px; height: 16px; border-radius: 50%; background: #fff; display: flex; align-items: center; justify-content: center; }
</style>
</head>
<body>
  <div class="masthead"></div>
  <div class="masthead-band"></div>
  <div class="masthead-rule"></div>

  <header>
    <div class="abs brand">
      <div class="brand-mark"></div>
      <div class="brand-name">Brightoak<br>Coatings</div>
    </div>

    <nav class="abs utility">
      <a class="current" href="#">Locations</a>
      <a href="#">Contact us</a><span class="sep">|</span>
      <a href="#">Jobs</a><span class="sep">|</span>
      <a href="#">Need Help</a>
    </nav>

    <div class="abs callout">
      <small>Call Now for a FREE ESTIMATE</small>
      <strong>(865) 555-0142</strong>
    </div>

    <div class="abs finder">
      <label>Find a local Brightoak Coatings Painter:</label>
      <div class="finder-row">
        <div class="finder-input">Enter Your Zip/Postal Code</div>
        <div class="finder-button">
          <svg width="10" height="10" viewBox="0 0 10 10"><circle cx="4" cy="4" r="3" fill="none" stroke="#fff" stroke-width="1.5"/><line x1="6.2" y1="6.2" x2="9" y2="9" stroke="#fff" stroke-width="1.6"/></svg>
          Search
        </div>
      </div>
    </div>

    <nav class="abs nav">
      <a class="active" href="#">HOME</a>
      <a href="#">SERVICES</a>
      <a href="#">FAQ</a>
      <a href="#">ABOUT US</a>
      <a href="#">GALLERY</a>
      <a href="#">REFERENCES</a>
      <a href="#">ESTIMATES</a>
      <a href="#">DESIGN TIPS</a>
      <a href="#">CONTACT US</a>
    </nav>
  </header>

  <section>
    <div class="abs hero" role="img" aria-label="Paint roller and brushes resting on an open colour swatch fan"></div>
    <div class="abs hero-tag">
      <span>Residential &amp;</span>
      <span class="accent">COMMERCIAL</span>
      <span>PAINTING</span>
    </div>
  </section>

  <section>
    <div class="abs welcome">
      <div class="welcome-inner">
        <div class="panel-title">Welcome to Brightoak Coatings !</div>
        <p>Lorem ipsum dolor sit amet, consectetur adipiscing elit. Quisque sit amet sem felis. Donec adipiscing, velit vitae malesuada bibendum, mauris tortor fermentum ante, eu sodales diam quam vitae libero. Quisque sceleri. Lorem ipsum dolor sit amet, consectetur adipiscing elit. Quisque sit amet sem felis. Donec adipiscing, velit vitae malesuada bibendum, mauris tortor fermentum ante,</p>
        <div class="more">▸ &nbsp;Read More</div>
      </div>
    </div>

    <div class="abs video" role="img" aria-label="Video still of the company's painting coach speaking to camera"></div>
    <div class="abs video-play">
      <svg width="12" height="12" viewBox="0 0 12 12"><polygon points="2,1 11,6 2,11" fill="#fff"/></svg>
    </div>
    <div class="abs video-caption">Knoxville Painting Tips</div>

    <form class="abs estimate">
      <div class="panel-title">Get a Free Estimate</div>
      <div class="abs field-label" style="left:9px;top:35px">Name</div>
      <div class="abs field" style="left:9px;top:51px;width:247px">Enter First Name</div>
      <div class="abs field-label" style="left:9px;top:86px">Email</div>
      <div class="abs field" style="left:9px;top:102px;width:130px">Enter Email Address</div>
      <div class="abs field-label" style="left:145px;top:86px">Mobile</div>
      <div class="abs field" style="left:145px;top:102px;width:111px">Enter Mobile Number</div>
      <div class="abs field-label" style="left:17px;top:137px">Resident Type</div>
      <div class="abs" style="left:17px;top:155px">
        <span class="radio"><i class="on"></i>Residentail</span>
        <span class="radio"><i></i>Commercial</span>
      </div>
      <div class="abs estimate-btn" style="left:188px;top:148px">Estimate</div>
    </form>
  </section>

  <section>
    <article class="abs story" style="left:179px">
      <div class="story-head">Our Painting In Knoxville
        <span class="story-arrow"><svg width="6" height="8" viewBox="0 0 6 8"><polyline points="1,1 5,4 1,7" fill="none" stroke="#fff" stroke-width="1.6"/></svg></span></div>
      <div class="story-body">
        <div class="story-thumb" role="img" aria-label="Painters on a lift working on a house gable" style="background:linear-gradient(160deg,#e6e2da,#b59a80 60%,#c4502a)"></div>
        <div><h4>Lorem ipsum dolor sit amet consec.</h4>
          <p>Lorem ipsum dolor sit amet, ctetur adiisc-ing elit. Quisque sit amet sem felis. Dc adipiscing, velit vitae malesuada.</p>
          <a href="#">Read More</a></div>
      </div>
    </article>

    <article class="abs story" style="left:456px;width:266px">
      <div class="story-head">East TN Painting Coach Training Videos
        <span class="story-arrow"><svg width="6" height="8" viewBox="0 0 6 8"><polyline points="1,1 5,4 1,7" fill="none" stroke="#fff" stroke-width="1.6"/></svg></span></div>
      <div class="story-body">
        <div class="story-thumb" role="img" aria-label="Two painters rolling paint onto an interior wall" style="background:linear-gradient(160deg,#d9d4c8,#9d9488 60%,#6e6558)"></div>
        <div><h4>Lorem ipsum dolor sit amet consec.</h4>
          <p>Lorem ipsum dolor sit amet, ctetur adiisc-ing elit. Quisque sit amet sem felis. Dc adipiscing, velit vitae malesuada.</p>
          <a href="#">Read More</a></div>
      </div>
    </article>

    <article class="abs story" style="left:744px">
      <div class="story-head">Our Painting In Knoxville
        <span class="story-arrow"><svg width="6" height="8" viewBox="0 0 6 8"><polyline points="1,1 5,4 1,7" fill="none" stroke="#fff" stroke-width="1.6"/></svg></span></div>
      <div class="story-body">
        <div class="story-thumb" role="img" aria-label="Freshly painted room with a red feature wall" style="background:linear-gradient(160deg,#e8c79a,#c2401e 55%,#8a2a14)"></div>
        <div><h4>Lorem ipsum dolor sit amet consec.</h4>
          <p>Lorem ipsum dolor sit amet, ctetur adiisc-ing elit. Quisque sit amet sem felis. Dc adipiscing, velit vitae malesuada.</p>
          <a href="#">Read More</a></div>
      </div>
    </article>
  </section>

  <footer>
    <div class="abs footer"></div>

    <div class="abs foot-col" style="left:180px">
      <h5>About Us</h5>
      <ul><li class="here">Home</li><li>Gallery</li><li>References</li><li>About Us</li></ul>
    </div>
    <div class="abs foot-col" style="left:325px">
      <h5>Services</h5>
      <ul><li>Residential</li><li>Commercial</li><li>Get a Estimate</li><li>Painting Tips</li></ul>
    </div>
    <div class="abs foot-col" style="left:478px">
      <h5 style="width:162px">Contact</h5>
      <ul><li>FAQ</li><li>Contact us</li><li>Locations</li><li>Mail</li></ul>
    </div>

    <div class="abs foot-side"></div>
    <blockquote class="abs quote">
      <em>Thanks Again</em>&nbsp; <u>The Hallorans</u><br>
      Thaks so much for your help. Several of my neighbors have commented on how good of a job you did.
    </blockquote>
    <div class="abs quote-badge"><div></div>Testimonial</div>

    <div class="abs foot-divide"></div>
    <div class="abs follow">
      <b>Follow Us</b>
      <i style="background:#3b5a9a"></i>
      <i style="background:#4fb3e8"></i>
      <i style="background:#2b6fc2"></i>
      <i style="background:#c3201f"></i>
    </div>
    <div class="abs foot-call">Call: (865) 555-0142</div>

    <div class="abs base">
      <div class="copy">© 2014 <b>Brightoak Coatings</b> All Rights Reserved</div>
      <div class="top">Back to Top
        <span><svg width="8" height="6" viewBox="0 0 8 6"><polyline points="1,5 4,1.5 7,5" fill="none" stroke="#888" stroke-width="1.6"/></svg></span>
      </div>
    </div>
  </footer>
</body>
</html>
```